Tidewell HVAC WordPress website design

Design a new modern, clean, website for HVAC mechanical business that uses company logo/colors for branding and recognition. Files attached are just for band and color information. Here is a website design that appeals to me https://www.quillerbyhomes.example/

A clear description of who we are and what we do

An easily-navigated site map

An easily-navigated site map for mobile devices

Easy-to-find contact information

Obvious call to action for service, installs or to schedule estimates

about us page

Provide a way for potential customers to contact us via text or email

provide a way that allows a customer to upload a picture to request a service call or quote.
Updates

I'm looking for the design to be completed in WordPress

Industry/Entity Type

HVAC Mechanical & Building Automation / Controls contractor

Coding

Coded - Design and coding required

Number of Pages Required

5+ page

Colors
0054AA
0677BA
7BADD7
CADEEF
E8F1F8

Requirements
Must have
• Design a new modern, clean, website for HVAC mechanical business that uses company logo/colors for branding and recognition. Files attached are just for band and color information. Here is a website design that appeals to me https://www.quillerbyhomes.example/ A clear description of who we are and what we do An easily-navigated site map An easily-navigated site map for mobile devices Easy-to-find contact information Obvious call to action for service, installs or to schedule estimates about us page Provide a way for potential customers to contact us via text or email provide a way that allows a customer to upload a picture to request a service call or quote.
Nice to have

```html
<!DOCTYPE html>
<html lang="en">
<head>
<meta charset="utf-8">
<title>Tidewell HVAC – Heating and Air Conditioning Services</title>
<link href="https://fonts.googleapis.com/css2?family=Poppins:wght@400;500;600;700&display=swap" rel="stylesheet">
<style>
:root{
  --navy:#0b3b7a;
  --navy-deep:#0d1b3d;
  --blue:#0054aa;
  --blue-mid:#0677ba;
  --blue-light:#7badd7;
  --ice:#cadeef;
  --mist:#e8f1f8;
  --gray-bg:#f2f2f2;
  --ink:#2b2b2b;
  --muted:#666;
  --star:#c8c400;
  --white:#fff;
}
*{box-sizing:border-box;margin:0;padding:0}
html,body{width:1200px;height:4751px;overflow:hidden}
body{font-family:'Poppins',sans-serif;color:var(--ink);background:var(--gray-bg);position:relative}
.abs{position:absolute}
a{color:inherit;text-decoration:none}

/* top bar */
.topbar{left:0;top:0;width:1200px;height:40px;background:var(--navy);color:#fff;font-size:15px;display:flex;align-items:center;padding:0 60px}
.topbar .item{display:flex;align-items:center;gap:10px;margin-right:70px}
.topbar .social{margin-left:auto;display:flex;gap:14px}
.topbar .social span{width:14px;height:14px;border-radius:50%;background:#fff;display:block}

/* nav */
.nav{left:0;top:40px;width:1200px;height:100px;background:#fff;font-size:18px;font-weight:500;color:#333}
.nav a{position:absolute;top:42px}
.brand{left:470px;top:8px;width:260px;height:86px;display:flex;align-items:center;justify-content:center;gap:10px;font-weight:700;font-size:26px;color:var(--navy)}
.brand i{width:20px;height:20px;border-radius:50%;background:var(--navy);display:block}

/* hero */
.hero{left:0;top:140px;width:1200px;height:568px;background:linear-gradient(90deg,#26456e 0%,#3d5f8c 40%,#6d8fb5 70%,#9fb7cf 100%)}
.hero h1{position:absolute;left:0;width:1200px;top:88px;text-align:center;color:#fff;font-size:54px;line-height:64px;font-weight:700}
.hero p{position:absolute;left:0;width:1200px;top:288px;text-align:center;color:#fff;font-size:23px;line-height:28px}
.hero .cta{position:absolute;left:399px;top:422px;width:402px;height:55px;background:var(--navy);color:#fff;font-size:21px;display:flex;align-items:center;justify-content:center}

.feature{width:258px;height:219px;background:#fff;border-radius:12px;box-shadow:0 2px 10px rgba(0,0,0,.08);text-align:center;top:656px}
.feature svg{margin-top:22px}
.feature h3{font-size:17px;font-weight:500;margin-top:10px;color:#222}
.feature p{font-size:9px;color:#888;margin-top:8px;line-height:15px;text-transform:uppercase}
.feature .more{font-size:13px;font-weight:600;color:var(--navy);margin-top:18px;display:flex;align-items:center;justify-content:center;gap:8px}

.photo{display:block}
.panel{background:#fff}
.panel h2{font-size:30px;font-weight:600;color:#222}
.panel p{font-size:13.5px;line-height:20px;color:#444}
.btn{background:var(--navy);color:#fff;font-size:13px;display:flex;align-items:center;justify-content:center;border-radius:4px}

/* services band */
.band{left:0;top:1976px;width:1200px;height:684px;background:var(--navy)}
.band h2{position:absolute;width:1200px;top:58px;text-align:center;color:#fff;font-size:28px;font-weight:600}
.svc{width:268px;height:361px;background:#fff;border-radius:10px;top:2138px}
.svc .img{position:absolute;left:14px;top:12px;width:240px;height:144px;border-radius:8px}
.svc .badge{position:absolute;left:34px;top:130px;width:56px;height:56px;border-radius:50%;background:var(--navy);border:4px solid #fff}
.svc h3{position:absolute;left:18px;top:200px;font-size:16px;font-weight:600}
.svc p{position:absolute;left:18px;top:228px;width:235px;font-size:10px;line-height:12px;color:#555}
.svc .more{position:absolute;left:18px;top:330px;font-size:10px;font-weight:600;color:var(--navy)}
.band .all{position:absolute;left:501px;top:584px;width:216px;height:44px;background:#fff;color:var(--navy);font-size:13px;display:flex;align-items:center;justify-content:center;border-radius:3px}

/* testimonials */
.clients{left:0;top:2660px;width:1200px;height:547px;background:#fff}
.clients h2{position:absolute;width:1200px;top:64px;text-align:center;font-size:29px;font-weight:600;color:#222}
.quote{width:260px;height:269px;background:#f5f5f5;border-radius:14px;top:2814px;text-align:center;box-shadow:0 4px 10px rgba(0,0,0,.05)}
.quote .avatar{width:64px;height:64px;border-radius:50%;background:linear-gradient(#6a5a52,#2e2a2a);margin:16px auto 0}
.quote h4{font-size:18px;font-weight:500;margin-top:12px}
.quote p{font-size:12px;line-height:19px;color:#555;margin:12px 26px 0}
.quote .stars{color:var(--star);font-size:26px;letter-spacing:6px;margin-top:12px}

.areas{display:grid;grid-template-columns:repeat(3,152px);row-gap:22px;margin-top:34px}
.areas span{display:flex;align-items:center;gap:10px;font-size:13px;color:#444}

.field{background:#f0f0f0;font-size:15px;color:#555;padding:0 12px;display:flex;align-items:center}

/* footer */
.footer{left:0;top:4276px;width:1200px;height:475px;background:var(--navy-deep);color:#fff}
.footer h4{position:absolute;top:62px;font-size:19px;font-weight:600}
.footer .col{position:absolute}
.footer .about{left:30px;top:148px;width:260px;font-size:14px;line-height:28px}
.footer .ci{position:absolute;font-size:14px;line-height:24px}
.footer .ci b{font-weight:600;display:block}
.footer .link{position:absolute;left:652px;width:270px;font-size:14px;border-bottom:1px solid rgba(255,255,255,.15);padding-bottom:8px;display:flex;justify-content:space-between}
.fs{position:absolute;top:359px;width:40px;height:40px;border-radius:50%;background:var(--blue)}
</style>
</head>
<body>

<div class="abs topbar">
  <span class="item"><svg width="15" height="11"><rect x="0.5" y="0.5" width="14" height="10" fill="#fff"/><path d="M1 1l6.5 5 6.5-5" stroke="#0b3b7a" fill="none"/></svg>info@website.com</span>
  <span class="item"><svg width="14" height="14" viewBox="0 0 24 24"><path fill="#fff" d="M6.6 10.8a15 15 0 006.6 6.6l2.2-2.2c.3-.3.7-.4 1-.2 1.1.4 2.3.6 3.6.6.6 0 1 .4 1 1V20c0 .6-.4 1-1 1A17 17 0 013 4c0-.6.4-1 1-1h3.5c.6 0 1 .4 1 1 0 1.3.2 2.5.6 3.6.1.3 0 .7-.2 1z"/></svg>(123) 456 7890</span>
  <span class="social"><span></span><span></span><span></span></span>
</div>

<nav class="abs nav" style="left:0">
  <a style="left:60px">HOME</a>
  <a style="left:178px">ABOUT</a>
  <a style="left:308px">SERVICES</a>
  <div class="abs brand"><i></i>Tidewell HVAC</div>
  <a style="left:752px">PRODUCTS</a>
  <a style="left:916px">FINANCING</a>
  <a style="left:1079px">BLOG</a>
</nav>

<section class="abs hero" role="img" aria-label="City skyline with modern office building, blue tint">
  <h1>HEATING AND<br>AIR CONDITIONING<br>SERVICES</h1>
  <p>Lorem ipsum dolor sit amet, consectetuer adipiscing elit.<br>Aenean commodo ligula eget dolor.<br>Aenean massa. Cum sociis natoque penatibus et<br>magnis dis parturient montes, nascetur ridiculus mus.</p>
  <a class="cta">CALL US NOW : (123) 456 7890</a>
</section>

<div class="abs feature" style="left:138px">
  <svg width="64" height="60" viewBox="0 0 64 60" fill="none" stroke="#0b3b7a" stroke-width="2.5"><rect x="6" y="18" width="30" height="32"/><path d="M12 18v32M18 18v32M24 18v32M30 18v32"/><path d="M36 30h10a8 8 0 000-16h-4"/><circle cx="46" cy="12" r="6"/></svg>
  <h3>Heating</h3>
  <p>Lorem ipsum dolor sit amet,<br>consectetuer adipiscing elit.</p>
  <div class="more">READ MORE <svg width="26" height="10"><path d="M0 5h22M17 1l5 4-5 4" stroke="#0b3b7a" stroke-width="2.5" fill="none"/></svg></div>
</div>
<div class="abs feature" style="left:475px">
  <svg width="64" height="60" viewBox="0 0 64 60" fill="none" stroke="#0b3b7a" stroke-width="2.5"><rect x="6" y="10" width="52" height="30" rx="3"/><circle cx="22" cy="25" r="9"/><path d="M22 16v18M13 25h18"/><path d="M38 20h14M38 26h14M38 32h14M16 46v8M26 46v8M36 46v8"/></svg>
  <h3>Cooling</h3>
  <p>Lorem ipsum dolor sit amet,<br>consectetuer adipiscing elit.</p>
  <div class="more">READ MORE <svg width="26" height="10"><path d="M0 5h22M17 1l5 4-5 4" stroke="#0b3b7a" stroke-width="2.5" fill="none"/></svg></div>
</div>
<div class="abs feature" style="left:816px">
  <svg width="64" height="60" viewBox="0 0 64 60" fill="none" stroke="#0b3b7a" stroke-width="2.5"><path d="M12 8l40 44M52 8L12 52"/><circle cx="12" cy="8" r="5"/><rect x="46" y="46" width="10" height="10"/></svg>
  <h3>Repairs</h3>
  <p>Lorem ipsum dolor sit amet,<br>consectetuer adipiscing elit.</p>
  <div class="more">READ MORE <svg width="26" height="10"><path d="M0 5h22M17 1l5 4-5 4" stroke="#0b3b7a" stroke-width="2.5" fill="none"/></svg></div>
</div>

<!-- who we are -->
<div class="abs photo" style="left:74px;top:957px;width:490px;height:363px;background:linear-gradient(120deg,#7d7a5c,#b89a82 55%,#e6d8cf)" role="img" aria-label="Technician in a cap working on equipment"></div>
<div class="abs panel" style="left:503px;top:1049px;width:562px;height:352px;padding:16px 50px 0 44px">
  <h2 style="margin-left:6px">WHO WE ARE</h2>
  <p style="margin-top:16px">Many business owners struggle to understand and maximize the true value of their businesses. This lack of awareness can lead to selling their business for less than it's worth, poor timing in the market, and inadequate preparation for the complexities of a business sale. They often face challenges in making their business attractive to buyers and aligning the sale with their personal and financial goals. This overall lack of preparedness and insight can result in significant financial and emotional regrets post-sale.</p>
  <a class="btn" style="width:216px;height:42px;margin-top:34px;margin-left:4px">MORE ABOUT US</a>
</div>

<!-- what we do -->
<div class="abs photo" style="left:577px;top:1511px;width:488px;height:363px;background:linear-gradient(150deg,#c8ccd0,#8a96a6 50%,#3f5a86)" role="img" aria-label="Two technicians in hard hats inspecting a ceiling duct"></div>
<div class="abs panel" style="left:74px;top:1581px;width:564px;height:354px;padding:20px 60px 0 44px">
  <h2 style="margin-left:6px">WHAT WE DO</h2>
  <p style="margin-top:16px">Many business owners struggle to understand and maximize the true value of their businesses. This lack of awareness can lead to selling their business for less than it's worth, poor timing in the market, and inadequate preparation for the complexities of a business sale. They often face challenges in making their business attractive to buyers and aligning the sale with their personal and financial goals. This overall lack of preparedness and insight can result in significant financial and emotional regrets post-sale.</p>
</div>

<!-- services -->
<section class="abs band"><h2>OUR SERVICES</h2>
  <a class="all">VIEW ALL SERVICES</a>
</section>
<div class="abs svc" style="left:122px">
  <div class="img" style="background:linear-gradient(135deg,#7a4a3a,#b1765a 50%,#3d5570)" role="img" aria-label="Gas fitting pipes and valves"></div>
  <div class="badge"></div>
  <h3>GAS FITTING</h3>
  <p>Lorem ipsum dolor sit amet, consectetuer adipiscing elit. Aenean commodo ligula eget dolor. Aenean massa. Cum sociis natoque penatibus et magnis dis parturient montes, nascetur ridiculus mus.</p>
  <div class="more">READ MORE ●</div>
</div>
<div class="abs svc" style="left:466px">
  <div class="img" style="background:linear-gradient(135deg,#8b6b52,#c9a68c 55%,#e9e2dc)" role="img" aria-label="Plumber fitting pipes"></div>
  <div class="badge"></div>
  <h3>PIPE FITTING</h3>
  <p>Lorem ipsum dolor sit amet, consectetuer adipiscing elit. Aenean commodo ligula eget dolor. Aenean massa. Cum sociis natoque penatibus et magnis dis parturient montes, nascetur ridiculus mus.</p>
  <div class="more">READ MORE ●</div>
</div>
<div class="abs svc" style="left:811px">
  <div class="img" style="background:linear-gradient(135deg,#4a4f55,#8d9297 50%,#d5d7d9)" role="img" aria-label="Technician installing an outdoor AC unit"></div>
  <div class="badge"></div>
  <h3>NEW INSTALLS</h3>
  <p>Lorem ipsum dolor sit amet, consectetuer adipiscing elit. Aenean commodo ligula eget dolor. Aenean massa. Cum sociis natoque penatibus et magnis dis parturient montes, nascetur ridiculus mus.</p>
  <div class="more">READ MORE ●</div>
</div>

<!-- testimonials -->
<section class="abs clients"><h2>WHAT OUR CLIENT SAYS</h2></section>
<div class="abs quote" style="left:123px"><div class="avatar" role="img" aria-label="Client portrait"></div><h4>John Doe</h4><p>Lorem ipsum dolor sit amet, consectetur adipiscing elit, sed do eiusmod tempor incididunt ut labore et dolore magna aliqua.</p><div class="stars">★★★★★</div></div>
<div class="abs quote" style="left:453px"><div class="avatar" role="img" aria-label="Client portrait"></div><h4>John Doe</h4><p>Lorem ipsum dolor sit amet, consectetur adipiscing elit, sed do eiusmod tempor incididunt ut labore et dolore magna aliqua.</p><div class="stars">★★★★★</div></div>
<div class="abs quote" style="left:781px"><div class="avatar" role="img" aria-label="Client portrait"></div><h4>John Doe</h4><p>Lorem ipsum dolor sit amet, consectetur adipiscing elit, sed do eiusmod tempor incididunt ut labore et dolore magna aliqua.</p><div class="stars">★★★★★</div></div>

<!-- areas -->
<div class="abs photo" style="left:112px;top:3277px;width:491px;height:363px;background:linear-gradient(135deg,#6d6a66,#c7b8a8 50%,#e4e4e2)" role="img" aria-label="Technician on a ladder drilling into a wall"></div>
<div class="abs panel" style="left:540px;top:3371px;width:564px;height:352px;padding:46px 0 0 76px">
  <h2>AREAS WE SERVED</h2>
  <div class="areas">
    <span><svg width="26" height="26"><circle cx="13" cy="13" r="11" fill="none" stroke="#0b3b7a" stroke-width="2"/><path d="M7 13h11M14 9l4 4-4 4" stroke="#0b3b7a" stroke-width="2" fill="none"/></svg>Area Name</span>
    <span><svg width="26" height="26"><circle cx="13" cy="13" r="11" fill="none" stroke="#0b3b7a" stroke-width="2"/><path d="M7 13h11M14 9l4 4-4 4" stroke="#0b3b7a" stroke-width="2" fill="none"/></svg>Area Name</span>
    <span><svg width="26" height="26"><circle cx="13" cy="13" r="11" fill="none" stroke="#0b3b7a" stroke-width="2"/><path d="M7 13h11M14 9l4 4-4 4" stroke="#0b3b7a" stroke-width="2" fill="none"/></svg>Area Name</span>
    <span><svg width="26" height="26"><circle cx="13" cy="13" r="11" fill="none" stroke="#0b3b7a" stroke-width="2"/><path d="M7 13h11M14 9l4 4-4 4" stroke="#0b3b7a" stroke-width="2" fill="none"/></svg>Area Name</span>
    <span><svg width="26" height="26"><circle cx="13" cy="13" r="11" fill="none" stroke="#0b3b7a" stroke-width="2"/><path d="M7 13h11M14 9l4 4-4 4" stroke="#0b3b7a" stroke-width="2" fill="none"/></svg>Area Name</span>
    <span><svg width="26" height="26"><circle cx="13" cy="13" r="11" fill="none" stroke="#0b3b7a" stroke-width="2"/><path d="M7 13h11M14 9l4 4-4 4" stroke="#0b3b7a" stroke-width="2" fill="none"/></svg>Area Name</span>
    <span><svg width="26" height="26"><circle cx="13" cy="13" r="11" fill="none" stroke="#0b3b7a" stroke-width="2"/><path d="M7 13h11M14 9l4 4-4 4" stroke="#0b3b7a" stroke-width="2" fill="none"/></svg>Area Name</span>
    <span><svg width="26" height="26"><circle cx="13" cy="13" r="11" fill="none" stroke="#0b3b7a" stroke-width="2"/><path d="M7 13h11M14 9l4 4-4 4" stroke="#0b3b7a" stroke-width="2" fill="none"/></svg>Area Name</span>
    <span><svg width="26" height="26"><circle cx="13" cy="13" r="11" fill="none" stroke="#0b3b7a" stroke-width="2"/><path d="M7 13h11M14 9l4 4-4 4" stroke="#0b3b7a" stroke-width="2" fill="none"/></svg>Area Name</span>
    <span><svg width="26" height="26"><circle cx="13" cy="13" r="11" fill="none" stroke="#0b3b7a" stroke-width="2"/><path d="M7 13h11M14 9l4 4-4 4" stroke="#0b3b7a" stroke-width="2" fill="none"/></svg>Area Name</span>
    <span><svg width="26" height="26"><circle cx="13" cy="13" r="11" fill="none" stroke="#0b3b7a" stroke-width="2"/><path d="M7 13h11M14 9l4 4-4 4" stroke="#0b3b7a" stroke-width="2" fill="none"/></svg>Area Name</span>
    <span><svg width="26" height="26"><circle cx="13" cy="13" r="11" fill="none" stroke="#0b3b7a" stroke-width="2"/><path d="M7 13h11M14 9l4 4-4 4" stroke="#0b3b7a" stroke-width="2" fill="none"/></svg>Area Name</span>
  </div>
</div>

<!-- contact -->
<div class="abs photo" style="left:614px;top:3788px;width:490px;height:363px;background:linear-gradient(135deg,#b7aa98,#d9d6d0 45%,#55606c)" role="img" aria-label="Outdoor AC unit with gauge tools"></div>
<div class="abs panel" style="left:112px;top:3819px;width:564px;height:396px">
  <h2 class="abs" style="left:44px;top:30px">CONTACT US NOW</h2>
  <div class="abs field" style="left:48px;top:86px;width:226px;height:36px">Name</div>
  <div class="abs field" style="left:292px;top:86px;width:226px;height:36px">Email</div>
  <div class="abs field" style="left:48px;top:138px;width:226px;height:36px">Phone</div>
  <div class="abs field" style="left:292px;top:138px;width:226px;height:36px">Service</div>
  <div class="abs field" style="left:48px;top:190px;width:470px;height:114px;align-items:flex-start;padding-top:10px">Message</div>
  <a class="abs btn" style="left:110px;top:329px;width:348px;height:43px;background:#1e4f8c">REQUEST A QUOTE NOW</a>
</div>

<!-- footer -->
<footer class="abs footer">
  <h4 style="left:30px">ABOUT US</h4>
  <h4 style="left:341px">CONTACT US</h4>
  <h4 style="left:652px">QUICK LINKS</h4>
  <h4 style="left:964px">OPENING HOURS</h4>
  <p class="col about">We are an award winning plumbing company with over 20 years experience in the business. We provide a wide range of services for both residential and commercial clients.</p>
  <span class="fs" style="left:30px"></span><span class="fs" style="left:82px"></span><span class="fs" style="left:134px"></span>

  <svg class="abs" style="left:344px;top:140px" width="20" height="26"><path d="M10 25s8-9 8-15a8 8 0 00-16 0c0 6 8 15 8 15z" fill="none" stroke="#7b8aa8" stroke-width="1.6"/><circle cx="10" cy="10" r="3" fill="none" stroke="#7b8aa8" stroke-width="1.6"/></svg>
  <div class="ci" style="left:388px;top:136px"><b>Address:</b>18 Harbor Lane, Brookvale, NY</div>
  <svg class="abs" style="left:342px;top:218px" width="24" height="20"><rect x="1" y="5" width="22" height="13" rx="2" fill="none" stroke="#7b8aa8" stroke-width="1.6"/><path d="M5 5c0-4 14-4 14 0" fill="none" stroke="#7b8aa8" stroke-width="1.6"/></svg>
  <div class="ci" style="left:388px;top:210px"><b>Phone:</b>+1123456789</div>
  <svg class="abs" style="left:346px;top:290px" width="16" height="26"><rect x="1" y="1" width="14" height="24" rx="2" fill="none" stroke="#7b8aa8" stroke-width="1.6"/></svg>
  <div class="ci" style="left:388px;top:284px"><b>Mobile:</b>+1123456789</div>
  <svg class="abs" style="left:342px;top:374px" width="24" height="18"><rect x="1" y="1" width="22" height="16" fill="none" stroke="#7b8aa8" stroke-width="1.6"/><path d="M1 1l11 9 11-9" fill="none" stroke="#7b8aa8" stroke-width="1.6"/></svg>
  <div class="ci" style="left:388px;top:358px"><b>Email:</b>support@tidewellhvac.example</div>

  <a class="link" style="top:146px">About<span>›</span></a>
  <a class="link" style="top:189px">Contact<span>›</span></a>
  <a class="link" style="top:231px">News List<span>›</span></a>
  <a class="link" style="top:273px">Services<span>›</span></a>
  <a class="link" style="top:315px">Shop<span>›</span></a>

  <svg class="abs" style="left:964px;top:142px" width="26" height="26"><circle cx="13" cy="13" r="12" fill="none" stroke="#4a5878" stroke-width="1.6"/><path d="M13 6v7h5" stroke="#4a5878" stroke-width="1.6" fill="none"/></svg>
  <div class="ci" style="left:1011px;top:136px"><b>Monday - Friday</b>8:00 AM - 5:00 PM</div>
  <svg class="abs" style="left:964px;top:216px" width="26" height="26"><circle cx="13" cy="13" r="12" fill="none" stroke="#4a5878" stroke-width="1.6"/><path d="M13 6v7h5" stroke="#4a5878" stroke-width="1.6" fill="none"/></svg>
  <div class="ci" style="left:1011px;top:210px"><b>Saturday</b>9:00 AM - 4:00 PM</div>
  <svg class="abs" style="left:964px;top:290px" width="26" height="26"><circle cx="13" cy="13" r="12" fill="none" stroke="#4a5878" stroke-width="1.6"/><path d="M13 6v7h5" stroke="#4a5878" stroke-width="1.6" fill="none"/></svg>
  <div class="ci" style="left:1011px;top:284px"><b>Sunday</b>CLOSED</div>
</footer>

</body>
</html>
```